We need letterhead, Business Cards, and envelops designed. We have attached a design of our logo and a sample of letterhead idea that was started but never perfected, it is only an idea for the letterhead if you can design something better we may love that also we are open to change.
We want a design that looks professional in style. we are a non profit trade association in the construction industry. the green color in the attached design represent green building, and we like that. also if you just want to enhance the letterhead sample that we attached that would be fine also.
Thanks and good luck
also the name that should show on the first business cards should be Merwin Haskell, Director are web address is www.vtqpa.org

```html
<!DOCTYPE html>
<html lang="en">
<head>
<meta charset="utf-8">
<title>Vista Trades Quality Partners Association – Envelope</title>
<link rel="stylesheet" href="https://fonts.googleapis.com/css2?family=Questrial&display=swap">
<style>
  :root {
    --paper: #deeab8;
    --ink-dark: #333333;
    --ink-green: #5e9b44;
    --window: #ffffff;
  }
  html, body {
    margin: 0;
    padding: 0;
    overflow: hidden;
    background: var(--paper);
  }
  .envelope {
    position: relative;
    width: 1200px;
    height: 781px;
    background: var(--paper);
    overflow: hidden;
    font-family: "Questrial", "Century Gothic", sans-serif;
  }
  .brand {
    position: absolute;
    left: 83px;
    top: 74px;
    display: flex;
    align-items: center;
    gap: 12px;
  }
  .brand-square {
    width: 20px;
    height: 20px;
    background: var(--ink-green);
  }
  .brand-name {
    font-size: 60px;
    line-height: 1;
    color: var(--ink-dark);
    letter-spacing: 1px;
  }
  .sender {
    position: absolute;
    right: 61px;
    top: 74px;
    margin: 0;
    text-align: right;
    font-style: normal;
    font-size: 15px;
    line-height: 18.5px;
    color: var(--ink-green);
  }
  .address-window {
    position: absolute;
    left: 78px;
    top: 461px;
    width: 668px;
    height: 247px;
    border-radius: 19px;
    background: var(--window);
  }
</style>
</head>
<body>
  <main class="envelope">
    <div class="brand">
      <span class="brand-name">VTQPA</span>
      <span class="brand-square"></span>
    </div>

    <address class="sender">
      Vista Trades Quality Partners Association<br>
      address: 4321 First Street<br>
      Any Town, State ZIP<br>
      Tel:<br>
      Fax:<br>
      Url: www.vtqpa.org
    </address>

    <div class="address-window"></div>
  </main>
</body>
</html>
```